Crispy Jerky Packaging for KO.MU

We need packaging for for our hand-crafted crispy beef jerky. We are launching a new product that is like eating a potato chip, but made of beef/pork. We would like to have a window for people to be able to see our product. It is a new type of jerky, so we need the audience to be able to see that they are getting value for what they are paying for. Where a traditional 1oz portion of jerky would have 10-11g protein, ours has 20g of protein. It is also easy on the jaw because there is no tearing off of the jerky, it eats just like a chip
Updates

Target Market(s)

Beer lovers/ health-conscious/ millenials

Industry/Entity Type

Product

Font styles to use
Other font styles liked:
• be creative

Colors
fbed22
9bcb3b
85cae6

Requirements
Must have
• Yellow packaging base
• 20g Protein per serving
• Made in Hawaii
Nice to have
• Would prefer the current font we have for the company name, KO.MU
Should not have
• cows

```html
<!DOCTYPE html>
<html lang="en">
<head>
<meta charset="UTF-8">
<title>KO.MU Crispy Beef Jerky Pouch</title>
<link href="https://fonts.googleapis.com/css2?family=Signika:wght@400;600;700&display=swap" rel="stylesheet">
<style>
  :root {
    --backdrop: #ebebeb;
    --pouch-black: #141414;
    --zip-line: #262626;
    --pouch-yellow: #f6c21c;
    --pouch-yellow-light: #fbd646;
    --ink: #0c0c0c;
    --brand-white: #ffffff;
    --jerky-dark: #3a1414;
    --jerky-mid: #6e2a22;
    --jerky-light: #8c4632;
  }
  html, body {
    margin: 0;
    padding: 0;
    width: 1200px;
    height: 1182px;
    overflow: hidden;
    background: var(--backdrop);
  }
  .canvas {
    position: relative;
    width: 1200px;
    height: 1182px;
    font-family: "Signika", sans-serif;
  }
  .pouch {
    position: absolute;
    left: 340px;
    top: 130px;
    width: 520px;
    height: 920px;
    border-radius: 18px 18px 10px 10px;
    overflow: hidden;
    background: linear-gradient(90deg, var(--pouch-yellow) 0%, var(--pouch-yellow-light) 55%, var(--pouch-yellow) 100%);
  }
  .pouch-top {
    position: absolute;
    left: 0;
    top: 0;
    width: 100%;
    height: 330px;
    background: linear-gradient(180deg, var(--pouch-black) 0%, var(--pouch-black) 80%, rgba(20,20,20,0) 100%);
  }
  .zip-line {
    position: absolute;
    left: 0;
    top: 100px;
    width: 100%;
    height: 4px;
    background: var(--zip-line);
  }
  .brand-name {
    position: absolute;
    left: 0;
    top: 150px;
    width: 100%;
    text-align: center;
    font-weight: 700;
    font-size: 116px;
    line-height: 1;
    letter-spacing: 2px;
    color: var(--brand-white);
    margin: 0;
  }
  .product-title {
    position: absolute;
    left: 0;
    top: 345px;
    width: 100%;
    text-align: center;
    font-weight: 700;
    font-size: 52px;
    line-height: 0.98;
    color: var(--ink);
    margin: 0;
  }
  .product-window {
    position: absolute;
    left: 180px;
    top: 470px;
    width: 310px;
    height: 420px;
    border-radius: 60px 20px 90px 40px;
    background: radial-gradient(ellipse at 40% 45%, var(--jerky-light) 0%, var(--jerky-mid) 45%, var(--jerky-dark) 100%);
  }
  .claims {
    position: absolute;
    z-index: 2;
    left: 36px;
    top: 815px;
    width: 130px;
    padding-left: 8px;
    border-left: 2px solid var(--ink);
    color: var(--ink);
  }
  .claims-protein {
    font-weight: 700;
    font-size: 26px;
    line-height: 1;
    margin: 0 0 4px;
  }
  .claims-line {
    font-weight: 600;
    font-size: 12px;
    line-height: 1.25;
    margin: 0;
    white-space: nowrap;
  }
</style>
</head>
<body>
<div class="canvas">
  <div class="pouch">
    <div class="pouch-top"></div>
    <div class="zip-line"></div>
    <h1 class="brand-name">KO.MU</h1>
    <h2 class="product-title">Crispy Beef<br>Jerky</h2>
    <div class="product-window" role="img" aria-label="Clear window showing crispy beef jerky pieces, shaped like the island of Hawaii"></div>
    <div class="claims">
      <p class="claims-protein">20g</p>
      <p class="claims-line">Protein per serving</p>
      <p class="claims-line">Made in Hawaii</p>
    </div>
  </div>
</div>
</body>
</html>
```